Parks Dept. Ad for Outside Exercise

We need a design for a 1/3 page ad in a regional fitness magazine. I got the initial design from one of our staffers at the parks dept. and knew we should/could find someone, and spend a little money to do better. I've uploaded the initial design to help with understanding the idea of what we're looking for, but feel free to go in a different direction. Obviously, less text! And I don't know why it has it twice...

people interested in fitness magazines

Fitness

• must provide a sense of why outdoor exercise is desirable and that the city of Riverbend City provides those benefits with our wonderful park system. Logo of the city (White or blue) and Parks and Rec contact info must be in ad, though certainly not as prominent as they had displayed in the initial ad.

```html
<!DOCTYPE html>
<html lang="en">
<head>
<meta charset="utf-8">
<title>Riverbend City Parks and Recreation – Benefits of Exercising in Nature</title>
<link rel="stylesheet" href="https://fonts.googleapis.com/css2?family=Anton&family=Bitter:ital,wght@1,800&family=Tinos:ital@1&family=Ubuntu:wght@500;700&display=swap">
<style>
  :root {
    --brand-blue: #253f8f;
    --headline-blue: #23409a;
    --white: #ffffff;
    --benefit-red: #d52b2b;
    --panel-white: rgba(255, 255, 255, 0.8);
    --leaf-bright: #c9d84a;
    --leaf-mid: #7f9a2c;
    --leaf-deep: #3f5a1f;
    --haze: #e9efd0;
    --path: #d9d4c4;
  }
  * { margin: 0; padding: 0; box-sizing: border-box; }
  html, body { width: 1195px; height: 1200px; overflow: hidden; background: var(--white); }
  .ad { position: relative; width: 1195px; height: 1200px; overflow: hidden; }

  .scene {
    position: absolute; inset: 0;
    background:
      radial-gradient(ellipse 240px 400px at 500px 720px, rgba(40,50,70,0.5), transparent 70%),
      radial-gradient(ellipse 520px 240px at 560px 1040px, var(--path), transparent 70%),
      radial-gradient(ellipse 460px 300px at 720px 180px, var(--haze), transparent 70%),
      radial-gradient(ellipse 380px 600px at 140px 420px, var(--leaf-bright), transparent 75%),
      linear-gradient(180deg, var(--leaf-mid) 0%, var(--leaf-deep) 60%, #6f8a38 100%);
  }

  .headline {
    position: absolute; left: 0; top: 48px; width: 1195px; text-align: center;
    font-family: "Anton", sans-serif; font-size: 92px; line-height: 110px;
    color: var(--headline-blue);
    text-shadow:
      3px 0 0 var(--white), -3px 0 0 var(--white), 0 3px 0 var(--white), 0 -3px 0 var(--white),
      2px 2px 0 var(--white), -2px -2px 0 var(--white), 2px -2px 0 var(--white), -2px 2px 0 var(--white);
  }

  .benefits {
    position: absolute; left: 660px; top: 230px; width: 500px;
    background: var(--panel-white); border-radius: 26px;
    padding: 30px 28px 30px 26px; list-style: none;
    font-family: "Bitter", serif; font-style: italic; font-weight: 800;
    font-size: 32px; line-height: 42px; color: var(--benefit-red);
  }
  .benefits li { position: relative; padding-left: 30px; }
  .benefits li + li { margin-top: 22px; }
  .benefits li::before {
    content: ""; position: absolute; left: 2px; top: 16px;
    width: 12px; height: 12px; border-radius: 50%; background: var(--benefit-red);
  }

  .invite {
    position: absolute; left: 40px; top: 700px; width: 320px; height: 320px;
    border-radius: 50%; background: var(--brand-blue); color: var(--white);
    font-family: "Tinos", serif; font-style: italic; font-size: 30px; line-height: 38px;
    text-align: center; display: flex; align-items: center; justify-content: center; padding: 0 30px;
  }

  .contact-bar {
    position: absolute; left: 0; top: 1070px; width: 1195px; height: 130px;
    background: var(--brand-blue); color: var(--white);
    font-family: "Ubuntu", sans-serif; display: flex; align-items: center; padding: 0 40px;
  }
  .city-mark { display: flex; align-items: center; gap: 14px; font-weight: 700; font-size: 34px; width: 300px; }
  .city-mark .dot { width: 22px; height: 22px; border-radius: 50%; background: var(--white); }
  .divider { width: 6px; height: 80px; margin: 0 36px 0 10px; }
  .dept-name { font-weight: 700; font-size: 28px; line-height: 38px; }
  .dept-lines { font-weight: 500; font-size: 24px; line-height: 34px; }
</style>
</head>
<body>
<main class="ad">
  <div class="scene" role="img" aria-label="Photo of a runner seen from behind on a sunlit path lined with green trees"></div>

  <h1 class="headline">Benefits of Exercising in Nature</h1>

  <ul class="benefits">
    <li>Healthier blood pressure and cholesterol</li>
    <li>Less stress, better mood</li>
    <li>More oxygen in fresh air</li>
    <li>Boosts well-being and self-esteem</li>
    <li>Natural Vitamin D</li>
  </ul>

  <p class="invite">30 miles of shared use trails, 4 fitness trails and scenic spots for yoga</p>

  <footer class="contact-bar">
    <div class="city-mark"><span class="dot"></span><span>Riverbend City</span></div>
    <svg class="divider" viewBox="0 0 6 80" aria-hidden="true">
      <g fill="#ffffff">
        <circle cx="3" cy="3" r="2.5"/><circle cx="3" cy="17" r="2.5"/><circle cx="3" cy="31" r="2.5"/>
        <circle cx="3" cy="45" r="2.5"/><circle cx="3" cy="59" r="2.5"/><circle cx="3" cy="73" r="2.5"/>
      </g>
    </svg>
    <div>
      <p class="dept-name">Riverbend City Parks and Recreation</p>
      <p class="dept-lines">555-204-7316 | rbcparks.org | parks@riverbend.gov</p>
    </div>
  </footer>
</main>
</body>
</html>
```